Business card - Brio Margin - size 85 mm * 55 mm

We need new business cards. Design must fit with our vision of the firm. You find in the attached file our logo and a short description of our firm (mission, vision, value, business and so on).

Target Market(s)

Consulting firm in performance improvement

Industry/Entity Type

Management Consulting

Contact Information for Business Card

SIZE
85 mm * 55 mm
INFORMATIONS
name surname
role position
telephone number
email address

Requirements
Must have
• the brand must APPEAR for the rest Would we like to have something sleek, inspired to a "just right" approach
Should not have
• Please avoid the black color as background

```html
<!DOCTYPE html>
<html lang="en">
<head>
<meta charset="utf-8">
<title>Brio Margin – Business Cards</title>
<link href="https://fonts.googleapis.com/css2?family=Montserrat:wght@400;500;600;700&display=swap" rel="stylesheet">
<style>
  :root {
    --stage: #e9e9e7;
    --card: #3e3e3f;
    --orange: #f26a1f;
    --white: #ffffff;
  }
  * { box-sizing: border-box; margin: 0; padding: 0; }
  html, body { width: 1200px; height: 900px; overflow: hidden; }
  body {
    background: var(--stage);
    font-family: "Montserrat", sans-serif;
    position: relative;
  }
  .card {
    position: absolute;
    width: 520px;
    height: 336px;
    background: var(--card);
    border-radius: 18px;
    overflow: hidden;
    box-shadow: 0 14px 34px rgba(0,0,0,.22);
  }
  .card-front { left: 70px; top: 90px; }
  .card-back { left: 610px; top: 474px; }
  .card-bands { position: absolute; inset: 0; width: 100%; height: 100%; }

  .brand-name {
    color: var(--orange); font-weight: 600; text-transform: uppercase;
    white-space: nowrap;
  }

  /* front */
  .front-brand {
    position: absolute; left: 0; right: 0; top: 96px;
    text-align: center; font-size: 30px; letter-spacing: 6px;
  }
  .front-web {
    position: absolute; left: 26px; bottom: 14px;
    color: var(--white); font-size: 15px; letter-spacing: .5px;
  }
  .front-web b { font-weight: 700; }

  /* back */
  .back-brand {
    position: absolute; left: 30px; top: 124px;
    font-size: 18px; letter-spacing: 10px;
  }
  .person {
    position: absolute; right: 28px; top: 34px; width: 210px; text-align: right;
    border-bottom: 1.5px solid var(--orange); padding-bottom: 6px;
  }
  .person-name {
    color: var(--orange); font-weight: 600; font-size: 19px; letter-spacing: 1px;
    text-transform: uppercase; white-space: nowrap;
  }
  .person-role { color: var(--white); font-size: 12px; margin-top: 2px; }
  .contacts {
    position: absolute; left: 30px; top: 196px; width: 230px;
    border-top: 1.5px solid var(--orange); padding-top: 10px;
    list-style: none;
  }
  .contacts li {
    display: flex; align-items: center; gap: 10px;
    color: var(--white); font-size: 13px; line-height: 22px;
  }
  .contacts svg { width: 12px; height: 12px; flex: none; }
  .contacts em { color: var(--orange); font-style: normal; font-weight: 600; }
</style>
</head>
<body>

<section class="card card-front" aria-label="Card front">
  <svg class="card-bands" viewBox="0 0 520 336" aria-hidden="true">
    <polygon points="262,294 520,274 520,283 300,301" fill="var(--white)"/>
    <polygon points="0,294 262,294 300,336 0,336" fill="var(--orange)"/>
  </svg>
  <p class="brand-name front-brand">Brio Margin</p>
  <p class="front-web">www.<b>briomargin</b>.com</p>
</section>

<section class="card card-back" aria-label="Card back">
  <svg class="card-bands" viewBox="0 0 520 336" aria-hidden="true">
    <polygon points="352,232 520,232 520,296 330,296" fill="var(--orange)"/>
    <polygon points="0,322 330,296 520,296 520,306 334,306 0,334" fill="var(--white)"/>
  </svg>
  <p class="brand-name back-brand">Brio Margin</p>
  <div class="person">
    <p class="person-name">Marco Linden</p>
    <p class="person-role">Director</p>
  </div>
  <ul class="contacts">
    <li>
      <svg viewBox="0 0 12 12"><path d="M2 1.5h2.2l1 2.6-1.3.9a6 6 0 0 0 3.1 3.1l.9-1.3 2.6 1V10a1 1 0 0 1-1 1A8.5 8.5 0 0 1 1 2.5a1 1 0 0 1 1-1z" fill="var(--orange)"/></svg>
      +330 2360-4817
    </li>
    <li>
      <svg viewBox="0 0 12 12"><rect x="1" y="2.5" width="10" height="7" rx="1" fill="none" stroke="var(--orange)" stroke-width="1.2"/><path d="M1.5 3l4.5 3.5L10.5 3" fill="none" stroke="var(--orange)" stroke-width="1.2"/></svg>
      info@briomargin.com
    </li>
    <li>
      <svg viewBox="0 0 12 12"><circle cx="6" cy="6" r="4.8" fill="none" stroke="var(--orange)" stroke-width="1.2"/><path d="M1.2 6h9.6M6 1.2c-2.4 2.8-2.4 6.8 0 9.6M6 1.2c2.4 2.8 2.4 6.8 0 9.6" fill="none" stroke="var(--orange)" stroke-width="1"/></svg>
      <span>www.<em>briomargin</em>.com</span>
    </li>
  </ul>
</section>

</body>
</html>
```